Book Cover Design Project - Pickup and Seduction Book Cover Needed

We are a small pickup and dating company based in Sydney, Australia called Copperfield Lantern Studio.
We have almost finished our first book that will be complete and printed in the very near future.
The title of the book will be:
"Quiet Harbour: Walking Calmly Through Mornings To Find Brighter Evenings"
With "Quiet Harbour" being the book title
and
"Walking Calmly Through Mornings To Find Brighter Evenings" being the tagline.
The book is about being honest, sincere and authentic when meeting and dating women and we require a book cover that makes a great first impression and excites guys while still being very classy and stylish.
We look forward to any and all submissions and we also look forward to choosing the best one from the submissions.
The book cover size is standard 6x9
The cover needs to be for epub AND printed books.
When designing this, design random blurb words. We will add this in later
Bleed for the book is atleast .125
The book is around 250 pages in size
The author''s name is Tobias Fenwright
Any other questions, please let me know
Reason: We want more submissions!

```html
<!DOCTYPE html>
<html lang="en">
<head>
<meta charset="UTF-8">
<title>Quiet Harbour – Book Cover</title>
<link rel="stylesheet" href="https://fonts.googleapis.com/css2?family=Montserrat:wght@500;800&family=Great+Vibes&display=swap">
<style>
  :root {
    --paper-light: #ffffff;
    --paper-shade: #ececed;
    --ink: #151515;
    --rule: #2a2a2a;
    --photo-hair: #4a3f3a;
    --photo-skin: #d8b8a2;
    --photo-shirt: #8c96a3;
    --photo-red: #c23a3e;
    --photo-denim: #a9b0b8;
    --photo-shoe: #8a6a4e;
  }
  html, body {
    margin: 0;
    padding: 0;
    width: 800px;
    height: 1200px;
    overflow: hidden;
  }
  .cover {
    position: relative;
    width: 800px;
    height: 1200px;
    overflow: hidden;
    background: radial-gradient(ellipse at 55% 50%, var(--paper-shade) 0%, #f4f4f5 45%, var(--paper-light) 80%);
    color: var(--ink);
  }
  .title-rule {
    position: absolute;
    top: 126px;
    height: 4px;
    background: var(--rule);
  }
  .title-rule--left { left: 0; width: 78px; }
  .title-rule--right { left: 720px; width: 80px; }
  .title-main {
    position: absolute;
    top: 68px;
    left: 0;
    width: 800px;
    margin: 0;
    text-align: center;
    font-family: "Montserrat", sans-serif;
    font-weight: 800;
    font-size: 118px;
    line-height: 1;
    letter-spacing: 3px;
  }
  .title-script {
    position: absolute;
    top: 176px;
    left: 130px;
    width: 540px;
    margin: 0;
    text-align: center;
    font-family: "Great Vibes", cursive;
    font-weight: 400;
    font-size: 106px;
    line-height: 1;
  }
  .cover-photo {
    position: absolute;
    left: 350px;
    top: 372px;
    width: 400px;
    height: 790px;
  }
  .tagline {
    position: absolute;
    top: 736px;
    left: 40px;
    width: 460px;
    margin: 0;
    text-align: center;
    font-family: "Montserrat", sans-serif;
    font-weight: 500;
    font-size: 29px;
    line-height: 48px;
    text-transform: uppercase;
  }
  .author {
    position: absolute;
    top: 1106px;
    left: 112px;
    margin: 0;
    font-family: "Montserrat", sans-serif;
    font-weight: 500;
    font-size: 27px;
    letter-spacing: 1px;
    text-transform: uppercase;
  }
</style>
</head>
<body>
  <main class="cover">
    <div class="title-rule title-rule--left"></div>
    <div class="title-rule title-rule--right"></div>
    <h1 class="title-main">QUIET</h1>
    <h2 class="title-script">Harbour:</h2>

    <svg class="cover-photo" viewBox="0 0 400 790" role="img" aria-label="Photograph of a couple embracing and kissing, the woman in a red dress and heels, the man in a checked shirt and jeans">
      <defs>
        <linearGradient id="photo-tones" x1="0" y1="0" x2="0" y2="1">
          <stop offset="0%" stop-color="var(--photo-hair)"/>
          <stop offset="14%" stop-color="var(--photo-skin)"/>
          <stop offset="28%" stop-color="var(--photo-shirt)"/>
          <stop offset="42%" stop-color="var(--photo-red)"/>
          <stop offset="58%" stop-color="var(--photo-denim)"/>
          <stop offset="78%" stop-color="var(--photo-skin)"/>
          <stop offset="100%" stop-color="var(--photo-shoe)"/>
        </linearGradient>
      </defs>
      <rect x="0" y="0" width="400" height="790" rx="36" fill="url(#photo-tones)" opacity="0.85"/>
    </svg>

    <p class="tagline">Walking calmly through mornings to find brighter evenings</p>
    <p class="author">By Tobias Fenwright</p>
  </main>
</body>
</html>
```